Velvor Display PowerPoint Design Project

We need PowerPoint slide templates for our Sales Media Kit at our re-branded company based in Canada called "Velvor Display Collective".

Looking for a look that clearly and powerfully portrays our unique and effective indoor advertising billboards in our network.

Our TinyPanes, WideSlats and GrandSheets are strategically placed in high traffic areas of restaurants, pubs, nightclubs, fitness clubs, colleges and universities, and sports arenas.

Key features of our media is a captive audience and 100% gender specific.

You can visit our old website for info on the above three media products (plorvex.ca)

Our Media Kits go out to small, medium business owners and advertising agenices.

Deliverables are:

1) Presentation cover slide with rich graphic content and space for content.
2) Presentation body slide with room for content 2 photos or logos. This slide should have the following:
a) No graphic in the text area
b) Space for page number at the bottom.
3) Photoshop (PSD) files for all graphic elements.
4) Font files for all fonts used.

Project Deadline Extended
Reason: Need more designs submitted.

We have uploaded our business card file.

Would like to incorporate the look, feel and colour of our business card to the power point template.

Target Market(s)

small business owners, marketing managers, media buyers and advertising agencies.

Industry/Entity Type

Advertising

Requirements
Must have
• We would like to see designs that:
- use the color scheme indicated by the attached logo design, perhaps expanding on it slightly.
- Look should be professional, smooth, and colourful.
-Must have a clean and modern feel that Ad Agencies would be impressed with.
-We have uploaded our business card file.

-Would like to incorporate the look, feel and colour of our business card to the power point template.

```html
<!DOCTYPE html>
<html lang="en">
<head>
<meta charset="utf-8">
<title>Velvor Display Collective – Slide Templates</title>
<link rel="stylesheet" href="https://fonts.googleapis.com/css2?family=Arimo:wght@400;700&family=Cormorant+Garamond:ital,wght@1,500&display=swap">
<style>
  :root {
    --page-bg: #dddddd;
    --slide-bg: #ffffff;
    --brand-blue: #2a68b1;
    --brand-grey: #8f8e8f;
    --mark-grey: #858485;
    --text-grey: #5a5a5a;
    --rule-grey: #6f6f6f;
    --white: #ffffff;
  }
  * { box-sizing: border-box; margin: 0; padding: 0; }
  html, body {
    width: 1200px; height: 839px; overflow: hidden;
    background: var(--page-bg);
    font-family: "Arimo", Arial, sans-serif;
  }
  .sheet { position: relative; width: 1200px; height: 839px; }
  .slide {
    position: absolute; width: 461px; height: 354px;
    background: var(--slide-bg); overflow: hidden;
    box-shadow: 0 0 1px rgba(0,0,0,0.15);
  }
  .slide--cover { left: 81px; top: 40px; }
  .slide--body  { left: 665px; top: 40px; width: 462px; }
  .slide--closing { left: 371px; top: 423px; height: 355px; }
  .slide__waves { position: absolute; inset: 0; width: 100%; height: 100%; }
  .wave-blue { fill: var(--brand-blue); }
  .wave-grey { fill: var(--brand-grey); }

  .brand {
    position: absolute; left: 82px; top: 32px;
    display: flex; align-items: center; gap: 12px;
  }
  .brand__square {
    width: 117px; height: 117px; border-radius: 14px;
    background: var(--mark-grey);
  }
  .brand__name {
    width: 180px;
    font-weight: 700; font-size: 34px; line-height: 1.08;
    color: var(--brand-blue);
  }

  .cover__text { position: absolute; left: 13px; bottom: 9px; color: var(--white); }
  .cover__title { font-size: 20px; font-weight: 700; line-height: 1.15; }
  .cover__subtitle { font-size: 16px; font-weight: 400; line-height: 1.2; }

  .body__header {
    position: absolute; left: 0; top: 0; width: 100%; height: 53px;
    border-bottom: 1px solid var(--rule-grey);
    padding: 13px 0 0 14px;
  }
  .body__title { font-size: 20px; font-weight: 700; color: var(--brand-blue); line-height: 1.1; }
  .body__subtitle { font-size: 12px; color: var(--text-grey); line-height: 1.2; }
  .body__list {
    position: absolute; left: 46px; top: 78px;
    list-style: none; font-size: 10.5px; color: var(--text-grey);
  }
  .body__list li { position: relative; padding-left: 12px; height: 20.8px; }
  .body__list li::before {
    content: ""; position: absolute; left: 1px; top: 4px;
    width: 5px; height: 5px; border-radius: 50%; background: var(--brand-blue);
  }

  .closing__thanks {
    position: absolute; left: 14px; bottom: 14px;
    font-family: "Cormorant Garamond", Georgia, serif;
    font-style: italic; font-weight: 500; font-size: 38px; color: var(--white);
  }
</style>
</head>
<body>
<main class="sheet">

  <section class="slide slide--cover">
    <svg class="slide__waves" viewBox="0 0 461 354" preserveAspectRatio="none" aria-hidden="true">
      <path class="wave-blue" d="M0,105 C40,215 160,288 275,288 C365,288 430,245 461,205 L461,216 C425,258 355,292 275,293 C150,294 40,228 0,126 Z"/>
      <path class="wave-grey" d="M0,158 C60,248 170,300 275,297 C365,295 430,262 461,222 L461,240 C420,276 350,302 275,303 C160,305 50,262 0,205 Z"/>
      <path class="wave-blue" d="M0,235 C100,272 200,302 280,304 C355,305 420,286 461,276 L461,354 L0,354 Z"/>
    </svg>
    <div class="brand">
      <span class="brand__square"></span>
      <span class="brand__name">Velvor Display Collective</span>
    </div>
    <div class="cover__text">
      <h1 class="cover__title">Click to add Title</h1>
      <p class="cover__subtitle">Click to add subtitle</p>
    </div>
  </section>

  <section class="slide slide--body">
    <svg class="slide__waves" viewBox="0 0 462 354" preserveAspectRatio="none" aria-hidden="true">
      <path class="wave-grey" d="M0,235 C70,300 170,340 270,338 C360,336 420,312 462,294 L462,304 C420,325 360,343 270,344 C160,345 60,310 0,263 Z"/>
      <path class="wave-blue" d="M0,303 C100,330 190,346 270,346 C360,346 420,335 462,328 L462,354 L0,354 Z"/>
    </svg>
    <header class="body__header">
      <h2 class="body__title">Enter your title here</h2>
      <p class="body__subtitle">Enter your subtitle here</p>
    </header>
    <ul class="body__list">
      <li>Lorem ipsum dolor sit amet, consectetur adipisicing elit,sed do eiusmod.</li>
      <li>Lorem ipsum dolor sit amet, consectetur adipisicing elit,sed do eiusmod.</li>
      <li>Lorem ipsum dolor sit amet, consectetur adipisicing elit,sed do eiusmod.</li>
      <li>Lorem ipsum dolor sit amet, consectetur adipisicing elit,sed do eiusmod.</li>
      <li>Lorem ipsum dolor sit amet, consectetur adipisicing elit,sed do eiusmod.</li>
      <li>Lorem ipsum dolor sit amet, consectetur adipisicing elit,sed do eiusmod.</li>
    </ul>
  </section>

  <section class="slide slide--closing">
    <svg class="slide__waves" viewBox="0 0 461 354" preserveAspectRatio="none" aria-hidden="true">
      <path class="wave-blue" d="M0,105 C40,215 160,288 275,288 C365,288 430,245 461,205 L461,216 C425,258 355,292 275,293 C150,294 40,228 0,126 Z"/>
      <path class="wave-grey" d="M0,158 C60,248 170,300 275,297 C365,295 430,262 461,222 L461,240 C420,276 350,302 275,303 C160,305 50,262 0,205 Z"/>
      <path class="wave-blue" d="M0,235 C100,272 200,302 280,304 C355,305 420,286 461,276 L461,354 L0,354 Z"/>
    </svg>
    <div class="brand">
      <span class="brand__square"></span>
      <span class="brand__name">Velvor Display Collective</span>
    </div>
    <p class="closing__thanks">Thank you!</p>
  </section>

</main>
</body>
</html>
```